Carrowell Business Card Re-design

Our current cards are outdated. This is our website www.carrowellinsights.example. We would like something that is "on-brand" and consistent with our social media sites. We are strategic consultants with a core competency in Marketing Research. Although, please know we are considering a brand logo redesign and potentially a new look. If we like your work here we will invite you to participate when we get to that project. Thank you very much. Harriet
Here are our social sites: https://twitter.com/Carrowell?lang=en
https://plus.google.com/+Carrowellinsights
https://www.linkedin.com/company/5094827/
https://www.facebook.com/CarrowellInc/
Business

```html
<!DOCTYPE html>
<html lang="en">
<head>
<meta charset="utf-8">
<title>Carrowell Business Card</title>
<link rel="stylesheet" href="https://fonts.googleapis.com/css2?family=Lato:wght@300;400;700&display=swap">
<style>
  :root {
    --stage: #f7851a;
    --card: #ffffff;
    --ink: #2b2b2b;
    --ink-soft: #555555;
    --accent: #f47b3a;
    --accent-light: #fbd1b3;
    --accent-pale: #fdeadb;
    --brand-green: #3fae3a;
  }
  * { box-sizing: border-box; margin: 0; padding: 0; }
  html, body {
    width: 1200px;
    height: 800px;
    overflow: hidden;
  }
  body {
    background: var(--stage);
    font-family: "Lato", Arial, sans-serif;
    color: var(--ink);
    position: relative;
  }
  .card {
    position: absolute;
    left: 320px;
    width: 560px;
    height: 320px;
    background: var(--card);
    overflow: hidden;
  }
  .card--front { top: 60px; }
  .card--back  { top: 420px; }

  .facet-field {
    position: absolute;
    top: 0;
    height: 100%;
  }
  .card--front .facet-field { right: 0; width: 300px; }
  .card--back  .facet-field { left: 0; width: 300px; }

  .holder {
    position: absolute;
    left: 47px;
    top: 46px;
  }
  .holder__name {
    font-weight: 700;
    font-size: 24px;
    letter-spacing: -0.3px;
    color: var(--ink);
    line-height: 1.1;
  }
  .holder__role {
    display: flex;
    align-items: center;
    gap: 14px;
    font-weight: 300;
    font-size: 21px;
    color: var(--ink-soft);
    margin-top: 4px;
  }
  .holder__rule {
    display: block;
    width: 46px;
    height: 3px;
    background: var(--accent);
  }

  .contacts {
    position: absolute;
    left: 47px;
    top: 154px;
    list-style: none;
  }
  .contacts__item {
    display: flex;
    align-items: center;
    gap: 22px;
    height: 30px;
    margin-bottom: 17px;
  }
  .contacts__icon {
    width: 30px;
    height: 30px;
    flex: none;
  }
  .contacts__text {
    font-weight: 700;
    font-size: 9.5px;
    line-height: 1.45;
    color: var(--ink);
  }

  .brand {
    position: absolute;
    left: 192px;
    top: 110px;
  }
  .brand__name {
    font-weight: 400;
    font-size: 62px;
    letter-spacing: 1px;
    color: var(--brand-green);
    line-height: 1;
  }
  .brand__phone {
    font-weight: 400;
    font-size: 21px;
    letter-spacing: 3px;
    color: var(--accent);
    margin-top: 2px;
  }
  .back__web {
    position: absolute;
    right: 62px;
    bottom: 28px;
    font-size: 13px;
    color: var(--ink);
  }
</style>
</head>
<body>

<section class="card card--front" aria-label="Card front">
  <svg class="facet-field" viewBox="0 0 300 320" role="img" aria-label="Faceted orange low-poly decoration">
    <defs>
      <linearGradient id="facetFront" x1="0" y1="0" x2="1" y2="0">
        <stop offset="0" stop-color="#fde3cc" stop-opacity="0.6"/>
        <stop offset="0.5" stop-color="#f9b98a"/>
        <stop offset="1" stop-color="#f28a4d"/>
      </linearGradient>
    </defs>
    <polygon points="90,0 300,0 300,320 90,320 130,250 110,180 150,110 120,50" fill="url(#facetFront)"/>
  </svg>

  <div class="holder">
    <h1 class="holder__name">DANIEL REYES</h1>
    <p class="holder__role">marketing officer <span class="holder__rule"></span></p>
  </div>

  <ul class="contacts">
    <li class="contacts__item">
      <svg class="contacts__icon" viewBox="0 0 30 30" aria-hidden="true">
        <circle cx="15" cy="15" r="13" fill="none" stroke="var(--accent)" stroke-width="2.2"/>
        <path d="M15 8a4.5 4.5 0 0 0-4.5 4.5c0 3.4 4.5 8.5 4.5 8.5s4.5-5.1 4.5-8.5A4.5 4.5 0 0 0 15 8z" fill="var(--ink)"/>
        <circle cx="15" cy="12.5" r="1.7" fill="#fff"/>
      </svg>
      <p class="contacts__text">Suite 12, Lakeview Road, Harbor City<br>North America, Florida</p>
    </li>
    <li class="contacts__item">
      <svg class="contacts__icon" viewBox="0 0 30 30" aria-hidden="true">
        <circle cx="15" cy="15" r="13" fill="none" stroke="var(--accent)" stroke-width="2.2"/>
        <path d="M10.5 9.5l2.3-.8 1.6 3-1.4 1.1a7 7 0 0 0 3.2 3.2l1.1-1.4 3 1.6-.8 2.3c-5 .6-9.6-4-9-9z" fill="var(--ink)"/>
      </svg>
      <p class="contacts__text">+ 1 555 014 2290<br>+ 1 555 014 2291</p>
    </li>
    <li class="contacts__item">
      <svg class="contacts__icon" viewBox="0 0 30 30" aria-hidden="true">
        <circle cx="15" cy="15" r="13" fill="none" stroke="var(--accent)" stroke-width="2.2"/>
        <circle cx="15" cy="15" r="7" fill="var(--ink)"/>
        <path d="M12 10.5c1.5.5 2 1.8 1 2.8s.5 2.2 1.8 2.5M17.5 13c1 .2 1.8 1 1.5 2.3M13 20c.3-1.3 1.3-2 2.5-1.8" stroke="#fff" stroke-width="1.1" fill="none"/>
      </svg>
      <p class="contacts__text">dreyes@carrowellinsights.example<br>www.carrowellinsights.example</p>
    </li>
  </ul>
</section>

<section class="card card--back" aria-label="Card back">
  <svg class="facet-field" viewBox="0 0 300 320" role="img" aria-label="Faceted orange low-poly decoration">
    <defs>
      <linearGradient id="facetBack" x1="0" y1="0" x2="1" y2="0">
        <stop offset="0" stop-color="#f28a4d"/>
        <stop offset="0.5" stop-color="#f9b98a"/>
        <stop offset="1" stop-color="#fde3cc" stop-opacity="0.6"/>
      </linearGradient>
    </defs>
    <polygon points="0,0 180,0 160,60 190,120 150,190 200,260 170,320 0,320" fill="url(#facetBack)"/>
  </svg>

  <div class="brand">
    <p class="brand__name">Carrowell</p>
    <p class="brand__phone">555.014.2290</p>
  </div>

  <p class="back__web">www.carrowellinsights.example</p>
</section>

</body>
</html>
```